wine label for a new vineyard

We have developing vineyard which is just starting production. It izs called Wattle Brook Vineyard. It's in rural Australia and the vineyard is on top of a hill where a prominent tree type is pine (technically Calitris). We want a wine label that incorporates these elements (pine trees, hill or ridge). The calitris pines are statuesque in shape, with sillouetes varying from Lombardy pines to Pencil pines. People often chose wines by the label and we are aiming for the upper end of the market so want a label which encourages buyers to believe that this is a sophisticated product. We need to be able to superimpose the grape variety, year and other information so it needs to be uncluttered design.

Target Market(s)

Experienced and discriminating wine drinkers. Prepared to pay $ 20 for a wine they appreciate.

Industry/Entity Type

Product

Requirements
Must have
• Some element of pines and ridge (or hill) so that people associate the name and the label design.
A label which leads the viewer to believe that this is a high quality product.
Nice to have
• We would like to be able to use some elements from the label as a logo.
Should not have
• Jokey wine labels are fashionable but we don't think they suit our segement of the market.

```html
<!DOCTYPE html>
<html lang="en">
<head>
<meta charset="utf-8">
<title>Wattle Brook Vineyard – Wine Labels</title>
<link rel="stylesheet" href="https://fonts.googleapis.com/css2?family=Libre+Baskerville&display=swap">
<style>
  :root {
    --page: #ffffff;
    --label-cream: #fcfaf2;
    --brand-grey: #86878a;
    --stripe-dark: #58585b;
    --merlot: #7e444a;
    --chardonnay: #858689;
    --label-text: #fcfaf2;
    --tree-tone: #f4f1e8;
  }
  html, body {
    margin: 0;
    padding: 0;
  }
  body {
    width: 1200px;
    height: 1000px;
    overflow: hidden;
    background: var(--page);
    position: relative;
    font-family: "Libre Baskerville", "Baskerville", Georgia, serif;
  }
  .wine-label {
    position: absolute;
    display: block;
  }
  .wine-label--feature { left: 248px; top: 497px; width: 220px; height: 275px; }
  .wine-label--merlot { left: 751px; top: 33px; width: 360px; height: 450px; }
  .wine-label--chardonnay { left: 751px; top: 508px; width: 360px; height: 450px; }

  .label-ground { fill: var(--label-cream); }
  .label-stripe { fill: var(--stripe-dark); }
  .label-field--merlot { fill: var(--merlot); }
  .label-field--chardonnay { fill: var(--chardonnay); }

  .brand-name {
    fill: var(--brand-grey);
    font-family: "Libre Baskerville", "Baskerville", Georgia, serif;
    font-weight: 400;
  }
  .brand-name__main { font-size: 33px; }
  .brand-name__sub { font-size: 13px; letter-spacing: 1.5px; }

  .vintage-year {
    fill: var(--label-text);
    font-family: "Libre Baskerville", "Baskerville", Georgia, serif;
    font-size: 16px;
    text-anchor: middle;
  }
  .variety-name {
    fill: var(--label-text);
    font-family: "Libre Baskerville", "Baskerville", Georgia, serif;
    font-size: 24px;
    text-anchor: middle;
  }
  .pine-illustration {
    fill: var(--tree-tone);
    opacity: 0.85;
  }
</style>
</head>
<body>

  <!-- Merlot label, featured -->
  <svg class="wine-label wine-label--feature" viewBox="0 0 360 450" aria-label="Wattle Brook Vineyard 2013 merlot label">
    <rect class="label-ground" x="0" y="0" width="360" height="450"/>
    <polygon class="label-stripe" points="0,434 360,74 360,450 0,450"/>
    <polygon class="label-field--merlot" points="16,450 360,106 360,450"/>
    <text class="brand-name">
      <tspan class="brand-name__main" x="38" y="118">wattle brook</tspan>
      <tspan class="brand-name__sub" x="104" y="146">VINEYARD</tspan>
    </text>
    <rect class="pine-illustration" x="308" y="285" width="22" height="137" role="img" aria-label="Slender line drawing of a callitris pine tree"/>
    <text class="vintage-year" x="237" y="373">2013</text>
    <text class="variety-name" x="237" y="405">merlot</text>
  </svg>

  <!-- Merlot label -->
  <svg class="wine-label wine-label--merlot" viewBox="0 0 360 450" aria-label="Wattle Brook Vineyard 2013 merlot label">
    <rect class="label-ground" x="0" y="0" width="360" height="450"/>
    <polygon class="label-stripe" points="0,434 360,74 360,450 0,450"/>
    <polygon class="label-field--merlot" points="16,450 360,106 360,450"/>
    <text class="brand-name">
      <tspan class="brand-name__main" x="38" y="118">wattle brook</tspan>
      <tspan class="brand-name__sub" x="104" y="146">VINEYARD</tspan>
    </text>
    <rect class="pine-illustration" x="308" y="285" width="22" height="137" role="img" aria-label="Slender line drawing of a callitris pine tree"/>
    <text class="vintage-year" x="237" y="373">2013</text>
    <text class="variety-name" x="237" y="405">merlot</text>
  </svg>

  <!-- Chardonnay label -->
  <svg class="wine-label wine-label--chardonnay" viewBox="0 0 360 450" aria-label="Wattle Brook Vineyard 2013 chardonnay label">
    <rect class="label-ground" x="0" y="0" width="360" height="450"/>
    <polygon class="label-stripe" points="0,434 360,72 360,450 0,450"/>
    <polygon class="label-field--chardonnay" points="16,450 360,104 360,450"/>
    <text class="brand-name">
      <tspan class="brand-name__main" x="38" y="118">wattle brook</tspan>
      <tspan class="brand-name__sub" x="104" y="146">VINEYARD</tspan>
    </text>
    <rect class="pine-illustration" x="308" y="285" width="22" height="137" role="img" aria-label="Slender line drawing of a callitris pine tree"/>
    <text class="vintage-year" x="212" y="373">2013</text>
    <text class="variety-name" x="212" y="405">chardonnay</text>
  </svg>

</body>
</html>
```